Business Name: MT Property Styling Pty Ltd

Business Type: Professional Home Styling and Minor Renovation Business

Logo: Attached is the logo that has been created.
I always envisaged the logo in the middle of the business card with my full name underneath it.

Maren Tulloch B.Com RVA DMH
Property Stylist & Project Manager

Include dot points of services
Staging Houses for Sale
Minor Home Renovations
Home Styling & Project Management
Re-Designing Living Spaces to Aid the Disabled

Somewhere on the card I would like to incorporate
"Property Styling and Cosmetic Renovations"

Colour Scheme:
Gloss black business card, with white and then
Gold or Silver as the highlight colours.

Incorporate a small amount of yellow only if possible to make it pop. If this really doesn’t work it doesn’t have to be used. Also l like the colour teal if that needs to be used as a contrast colour.

Feel/Themes
• I love antique chairs, regal expensive looking furniture mixed with modern homes (this is the unique style I want to sell) antique and modern mix that looks high class as well as modern and fresh, targeting an executive market.
• I want to use an orchid as a trademark throughout the course of my work, not sure if this can somehow be incorporated? Also really like crowns to give that regal/antique feel and then something else to give that modern twist (I don’t know what the something else could be)
• Wall Paper Look (on a portion of it not all of it, like a French look)
• Overall feel - A very deluxe and professional feel with a little bit of creative flare.

I hope this helps create a bit of a picture.

Is it ok that I call you tomorrow morning? My mobile number is 0491 862 574 if you have any questions for me in the meantime.

Target Market(s)

High Quality Executive Market - People selling homes

Industry/Entity Type

Business

Contact Information for Business Card

Include dot points of services:
Staging Houses for Sale
Minor Home Renovations

Font styles to use
Serif
Script

Colors
33b8a4
fbed22

Requirements
Must have
• Maren Tulloch B.Com RVA DMH
• Property Stylist & Project Manager
• RVA and DMH Logos on the card
• "Dramatically increase the value of your property"
Nice to have
• Colour Scheme:
• Gloss black business card, with white and then
• Gold or Silver as the highlight colours.
• Incorporate a small amount of yellow only if possible to make it pop. If this really doesn’t work it doesn’t have to be used. Also l like the colour teal if that needs to be used as a contrast colour.
• Also like teal as a highlight colour.

```html
<!DOCTYPE html>
<html lang="en">
<head>
<meta charset="utf-8">
<title>MT Property Styling Pty Ltd – Business Card</title>
<link rel="stylesheet" href="https://fonts.googleapis.com/css2?family=Cinzel:wght@400;600&family=Parisienne&family=Lato:ital,wght@0,400;1,400&display=swap">
<style>
  :root {
    --backdrop: #a9a9a9;
    --card-black: #0b0b0b;
    --card-black-sheen: #2a2a2a;
    --card-white: #ffffff;
    --gold-dark: #5e4a12;
    --gold-mid: #9c7d24;
    --gold-light: #c9a94a;
    --ink: #1d1d1d;
    --ink-soft: #3a3a3a;
    --silver: #b9b9b9;
    --rule-light: #e8e8e8;
  }
  html, body {
    margin: 0;
    width: 1200px;
    height: 871px;
    overflow: hidden;
    background: radial-gradient(ellipse at 50% 45%, #c4c4c4 0%, var(--backdrop) 60%, #8c8c8c 100%);
  }
  .canvas {
    position: relative;
    width: 1200px;
    height: 871px;
    display: flex;
    justify-content: center;
    align-items: center;
    gap: 50px;
  }
  .card {
    position: relative;
    width: 540px;
    height: 330px;
    border-radius: 4px;
    overflow: hidden;
    box-shadow: 0 14px 30px rgba(0,0,0,0.35);
  }

  /* Back: gloss black */
  .card-back {
    background: linear-gradient(160deg, var(--card-black-sheen) 0%, var(--card-black) 35%, #151515 70%, var(--card-black) 100%);
  }
  .tagline {
    position: absolute;
    left: 0; right: 0;
    text-align: center;
    font-family: "Parisienne", cursive;
    color: #f2f2f2;
    margin: 0;
  }
  .tagline-top { top: 36px; font-size: 30px; color: var(--silver); }
  .tagline-main { top: 78px; font-size: 44px; }
  .service-band {
    position: absolute;
    left: 0; right: 0;
    top: 160px;
    height: 118px;
    background: linear-gradient(180deg, var(--gold-light) 0%, var(--gold-mid) 40%, var(--gold-dark) 100%);
    border-top: 2px solid var(--rule-light);
    border-bottom: 2px solid var(--rule-light);
  }
  .service-list {
    list-style: none;
    margin: 0;
    padding: 0;
    position: absolute;
    inset: 22px 26px;
    display: grid;
    grid-template-columns: 0.8fr 1.2fr;
    grid-auto-flow: column;
    grid-template-rows: 1fr 1fr;
    row-gap: 10px;
    column-gap: 10px;
  }
  .service-item {
    display: flex;
    align-items: center;
    gap: 10px;
    font-family: "Lato", sans-serif;
    font-size: 14px;
    color: #f7f2e2;
    white-space: nowrap;
  }
  .tick { width: 16px; height: 16px; flex: none; }

  /* Front: white */
  .card-front { background: var(--card-white); }
  .brand-mark {
    position: absolute;
    top: 62px;
    left: 0; right: 0;
    display: flex;
    justify-content: center;
    align-items: center;
    gap: 12px;
  }
  .brand-dot {
    width: 12px; height: 12px;
    border-radius: 50%;
    background: var(--silver);
  }
  .brand-name {
    font-family: "Cinzel", serif;
    font-weight: 400;
    font-size: 17px;
    letter-spacing: 1.5px;
    color: var(--ink-soft);
    text-transform: uppercase;
  }
  .holder {
    position: absolute;
    top: 140px;
    left: 0; right: 0;
    text-align: center;
  }
  .holder-name {
    margin: 0;
    font-family: "Cinzel", serif;
    font-weight: 600;
    font-size: 22px;
    color: var(--ink);
    letter-spacing: 0.5px;
  }
  .holder-role {
    margin: 6px 0 0;
    font-family: "Lato", sans-serif;
    font-style: italic;
    font-size: 16px;
    color: var(--ink-soft);
  }
  .footer-band {
    position: absolute;
    left: 0; right: 0; bottom: 0;
    height: 58px;
    background: linear-gradient(180deg, var(--gold-light) 0%, var(--gold-mid) 45%, var(--gold-dark) 100%);
    border-top: 4px solid var(--ink);
  }
</style>
</head>
<body>
<main class="canvas">
  <section class="card card-back" aria-label="Business card back">
    <p class="tagline tagline-top">Property Styling</p>
    <p class="tagline tagline-main">and Cosmetic Renovations</p>
    <div class="service-band">
      <ul class="service-list">
        <li class="service-item">
          <svg class="tick" viewBox="0 0 16 16"><path d="M2 8.5 L6 12.5 L14 3" fill="none" stroke="#f7f2e2" stroke-width="2"/></svg>
          Staging Houses for Sale
        </li>
        <li class="service-item">
          <svg class="tick" viewBox="0 0 16 16"><path d="M2 8.5 L6 12.5 L14 3" fill="none" stroke="#f7f2e2" stroke-width="2"/></svg>
          Minor Home Renovations
        </li>
        <li class="service-item">
          <svg class="tick" viewBox="0 0 16 16"><path d="M2 8.5 L6 12.5 L14 3" fill="none" stroke="#f7f2e2" stroke-width="2"/></svg>
          Home Styling &amp; Project Management
        </li>
        <li class="service-item">
          <svg class="tick" viewBox="0 0 16 16"><path d="M2 8.5 L6 12.5 L14 3" fill="none" stroke="#f7f2e2" stroke-width="2"/></svg>
          Re-Designing Living Spaces to Aid the Disabled
        </li>
      </ul>
    </div>
  </section>

  <section class="card card-front" aria-label="Business card front">
    <div class="brand-mark">
      <span class="brand-dot"></span>
      <span class="brand-name">MT Property Styling Pty Ltd</span>
    </div>
    <div class="holder">
      <h1 class="holder-name">Maren Tulloch B.Com RVA DMH</h1>
      <p class="holder-role">Property Stylist &amp; Project Manager</p>
    </div>
    <div class="footer-band"></div>
  </section>
</main>
</body>
</html>
```